Junk Removal company with existing WordPress website needs new mobile enhanced website

I am looking to have someone take my existing website and either update it with a new design and menu which is more mobile enhanced (70% of my traffic is from mobile devices and most people stay on the home page to find what they need) or create a new website from scratch to achieve my design goals. My name goal is the have to home page be quick and easy to find what the customer is looking for.
Our current website is: BrightmoorJunkCarters.com and Google my business page https://g.page/brightmoorjunkcarters
I have attached an example the design idea I came up with for the home page based on what I would like it to look like as well as some logo files and pictures.

```html
<!DOCTYPE html>
<html lang="en">
<head>
<meta charset="utf-8">
<title>Brightmoor Junk Carters – Mobile Home Page</title>
<link href="https://fonts.googleapis.com/css2?family=Outfit:wght@300;400;500;600;700;800&display=swap" rel="stylesheet">
<style>
:root{
  --board:#e6e6e6;
  --ink:#1b1b1b;
  --text:#3a3a3a;
  --muted:#8a8a8a;
  --orange:#ff9500;
  --hero-blue:#6c8fe0;
  --night:#101820;
  --night-2:#1e2d3d;
  --soft:#f6f6fb;
  --white:#ffffff;
}
*{box-sizing:border-box;margin:0;padding:0}
html,body{width:1200px;height:2915px;overflow:hidden}
body{background:var(--board);font-family:'Outfit',sans-serif;color:var(--text);position:relative}
.abs{position:absolute}
.board-label{position:absolute;left:36px;top:413px;transform-origin:0 0;transform:rotate(-90deg);font-size:122px;font-weight:800;color:var(--ink);letter-spacing:-2px;line-height:1}

/* home screen */
.screen-home{position:absolute;left:190px;top:60px;width:428px;height:2824px;background:var(--white);overflow:hidden}
.status-bar{position:absolute;left:0;top:0;width:100%;height:23px;background:#1f3a8a;color:#fff;font-size:13px;display:flex;align-items:center;justify-content:space-between;padding:0 10px}
.site-header{position:absolute;left:0;top:23px;width:100%;height:61px;background:#111;z-index:2}
.menu-icon{position:absolute;left:22px;top:22px;width:22px}
.menu-icon span{display:block;height:2px;background:#fff;margin-bottom:5px}
.brand{position:absolute;left:150px;top:10px;width:128px;text-align:center;color:#fff;font-weight:700;font-size:13px;line-height:15px;letter-spacing:.5px;display:flex;flex-direction:column;align-items:center;gap:4px}
.brand-dot{width:14px;height:14px;border-radius:50%;background:var(--orange)}
.btn-estimate{position:absolute;left:314px;top:15px;width:98px;height:28px;background:var(--orange);color:#fff;font-size:11px;font-weight:600;border-radius:2px;display:flex;align-items:center;justify-content:center}
.hero{position:absolute;left:0;top:84px;width:100%;height:398px;background:var(--hero-blue);border-radius:0 0 50% 50%/0 0 34px 34px;overflow:hidden}
.hero-title{position:absolute;top:92px;width:100%;text-align:center;color:#fff;font-size:29px;font-weight:300;letter-spacing:-.3px}
.hero-title strong{font-weight:700}
.hero-sub{position:absolute;top:131px;width:100%;text-align:center;color:#fff;font-size:12px}
.btn-call{position:absolute;left:132px;top:174px;width:164px;height:27px;background:var(--orange);color:#fff;font-size:8px;border-radius:2px;display:flex;align-items:center;justify-content:center;gap:7px}
.hero-photo{position:absolute;left:0;top:224px;width:100%;height:174px;background:linear-gradient(180deg,#6c8fe0 0%,#8ea3c8 35%,#4c5a3f 55%,#2b2b2b 80%,#3b3632 100%);border-bottom:3px solid #2a2a2a}
.dash{position:absolute;width:30px;height:2px;background:var(--orange)}
.sec-title{position:absolute;width:100%;text-align:center;color:var(--ink)}
.intro-text{position:absolute;top:877px;left:30px;width:368px;text-align:center;font-size:11px;line-height:22px;color:var(--text)}
.btn-book{position:absolute;left:143px;top:981px;width:139px;height:31px;border:1.5px solid var(--orange);border-radius:16px;font-size:12px;font-weight:500;color:var(--ink);display:flex;align-items:center;justify-content:center}
.badge-exp{position:absolute;left:67px;top:754px;width:75px;height:28px;background:var(--orange);color:#fff;display:flex;align-items:center;gap:5px;padding-left:6px;font-size:11px;font-weight:600}
.badge-exp small{font-size:7px;font-weight:400;line-height:8px}
.services{position:absolute;left:0;top:1053px;width:100%;height:1771px;background:var(--soft)}
.service{position:absolute;left:0;width:100%;height:544px}
.service-hex{position:absolute;left:70px;top:0;width:270px;height:260px;overflow:visible}
.service-title{position:absolute;top:296px;width:100%;text-align:center;font-size:25px;font-weight:500;color:var(--ink)}
.service-rule{position:absolute;left:57px;top:343px;width:331px;border-top:1.5px dotted #9a9aa5}
.service-list{position:absolute;top:367px;left:57px;width:360px;list-style:none;display:grid;grid-template-columns:191px 169px;row-gap:8px}
.service-list li{font-size:13px;color:var(--text);position:relative;padding-left:19px;line-height:18px}
.service-list li::before{content:"";position:absolute;left:0;top:5px;width:7px;height:7px;border-radius:50%;background:var(--orange)}
.squiggle{position:absolute;left:180px;top:483px}

/* contact screen */
.screen-contact{position:absolute;left:686px;top:60px;width:429px;height:1174px;background:var(--white);overflow:hidden}
.quote-card{position:absolute;left:47px;top:55px;width:328px;height:166px;background:#fff;box-shadow:0 0 14px rgba(0,0,0,.07)}
.quote-mark{position:absolute;left:22px;top:20px;font-size:40px;font-weight:800;color:var(--orange);line-height:1}
.quote-text{position:absolute;left:55px;top:22px;width:250px;font-size:10.5px;line-height:19.5px;color:#555}
.avatar{position:absolute;left:62px;top:249px;width:40px;height:40px;border-radius:50%;background:radial-gradient(circle,#6b7c8f,#2a3a48);border:2px solid #e3b200}
.reviewer{position:absolute;left:117px;top:253px;font-size:10px;font-weight:600;color:var(--ink);letter-spacing:.3px}
.reviewer small{display:block;font-size:9px;font-weight:400;color:var(--muted);margin-top:4px;letter-spacing:0}
.dots{position:absolute;left:201px;top:309px;display:flex;gap:5px}
.dots span{width:9px;height:9px;border-radius:50%;border:1px solid #777}
.dots span.on{background:var(--orange);border-color:var(--orange)}
.divider-orange{position:absolute;left:0;top:364px;width:100%;height:3px;background:var(--orange)}
.contact-title{position:absolute;top:408px;width:100%;text-align:center;font-size:27px;font-weight:700;color:var(--ink)}
.contact-sub{position:absolute;top:442px;width:100%;text-align:center;font-size:12.5px}
.form-lead{position:absolute;left:51px;top:485px;font-size:14px;color:var(--ink)}
.field{position:absolute;left:50px;width:329px;border:1px solid #c9c9c9;border-radius:2px;font-size:9.5px;color:#999;padding:8px 14px}
.btn-submit{position:absolute;left:271px;top:730px;width:108px;height:28px;background:var(--orange);color:#fff;font-size:12px;font-weight:600;display:flex;align-items:center;justify-content:center}
.footer{position:absolute;left:0;top:722px;width:100%;height:452px;background:linear-gradient(180deg,var(--night-2),var(--night) 70%)}
.footer-card{position:absolute;left:20px;top:367px;width:388px;height:411px;background:#fff}
.footer-brand{position:absolute;top:828px;width:100%;display:flex;flex-direction:column;align-items:center;gap:8px;color:#fff;font-weight:700;font-size:16px;line-height:19px;letter-spacing:.5px;text-align:center}
.footer-brand i{width:22px;height:22px;border-radius:50%;background:var(--orange)}
.footer-text{position:absolute;top:918px;left:60px;width:309px;text-align:center;color:#d5dbe3;font-size:11px;line-height:19px}
.foot-head{position:absolute;top:1001px;font-size:12px;font-weight:700;color:#fff}
.foot-links{position:absolute;left:31px;top:1035px;font-size:12px;color:#dfe4ea;line-height:22px}
.foot-links span{margin:0 10px}
.newsletter-label{position:absolute;left:239px;top:1034px;font-size:10.5px;color:#dfe4ea}
.newsletter{position:absolute;left:239px;top:1055px;width:164px;height:23px;background:#fff;display:flex;justify-content:flex-end}
.newsletter b{width:64px;background:var(--orange);color:#fff;font-size:10px;font-weight:400;display:flex;align-items:center;justify-content:center}
.footer-bottom{position:absolute;left:0;top:1106px;width:100%;height:68px;background:#000;border-top:1px solid #333}
.copyright{position:absolute;left:31px;top:24px;font-size:10px;color:#ddd}
.social{position:absolute;left:327px;top:19px;display:flex;gap:5px}
.social span{width:22px;height:22px;border-radius:50%;border:1px solid #ddd}
</style>
</head>
<body>
<div class="board-label">Mobile</div>

<section class="screen-home">
  <div class="status-bar"><span>●●●○○ LINKA</span><span>4:21 PM</span><span>100% ▭</span></div>
  <div class="hero">
    <div class="hero-title">Best Rated <strong>JUNK REMOVEL</strong></div>
    <div class="hero-sub">&amp; Property Cleanout Company in the Brightmoor valley</div>
    <div class="btn-call">
      <svg width="10" height="10" viewBox="0 0 24 24"><path fill="#fff" d="M6.6 10.8a15 15 0 0 0 6.6 6.6l2.2-2.2a1 1 0 0 1 1-.25 11.4 11.4 0 0 0 3.6.6 1 1 0 0 1 1 1V20a1 1 0 0 1-1 1A17 17 0 0 1 3 4a1 1 0 0 1 1-1h3.5a1 1 0 0 1 1 1c0 1.25.2 2.45.6 3.6a1 1 0 0 1-.25 1z"/></svg>
      CALL US NOW (555) 014 2273
    </div>
    <div class="hero-photo" role="img" aria-label="Company box truck and pickup parked on a lawn under a blue sky"></div>
  </div>
  <header class="site-header">
    <div class="menu-icon"><span></span><span></span><span></span></div>
    <div class="brand"><i class="brand-dot"></i>BRIGHTMOOR<br>JUNK CARTERS</div>
    <div class="btn-estimate">Free Estimate</div>
  </header>

  <div class="dash" style="left:199px;top:518px"></div>
  <h2 class="sec-title" style="top:528px;font-size:20px;font-weight:500">Junk Removal and Hauling</h2>
  <p class="sec-title" style="top:560px;font-size:12px;line-height:18px;color:var(--text)">The Best Rated Junk Hauling and Cleanout<br>Service in the Harlow Metro area.</p>

  <div class="abs" style="left:206px;top:616px;width:173px;height:226px;border-radius:50%;background:#f3f3f9"></div>
  <svg class="abs" style="left:124px;top:638px" width="197" height="208" viewBox="0 0 197 208" role="img" aria-label="Owner standing beside the company box truck">
    <defs><linearGradient id="g-intro" x1="0" y1="0" x2="0" y2="1"><stop offset="0" stop-color="#8aa6d9"/><stop offset=".5" stop-color="#c9cdd2"/><stop offset="1" stop-color="#3a3a3a"/></linearGradient></defs>
    <polygon points="98.5,3 194,55 194,153 98.5,205 3,153 3,55" fill="url(#g-intro)" stroke="#1b1b1b" stroke-width="4"/>
  </svg>
  <div class="badge-exp">10+<small>Years<br>Experience</small></div>

  <p class="intro-text">Fastest Response time with Same Day &amp; Next Day service available. We're the Friendliest and Most Professional junk haulers serving Harlow, Kestrel, Ashford, Pine Hollow, Millbrook, Carver, Dunmore, Larkspur and all of the Brightmoor Valley. Call us Today ! 555-014-2273</p>
  <div class="btn-book">Book Service Now</div>

  <section class="services">
    <h2 class="sec-title" style="top:52px;font-size:29px;font-weight:500">Our Services</h2>
    <p class="sec-title" style="top:88px;font-size:11px;color:var(--text)">Lorem Ipsum is simply dummy text of the printing.</p>
    <div class="dash" style="left:199px;top:115px"></div>

    <article class="service" style="top:137px">
      <svg class="service-hex" viewBox="0 0 270 260" role="img" aria-label="Pile of household junk, wood and old tires">
        <defs><linearGradient id="g-junk" x1="0" y1="0" x2="0" y2="1"><stop offset="0" stop-color="#5d7a3a"/><stop offset=".5" stop-color="#8a7a66"/><stop offset="1" stop-color="#3b3530"/></linearGradient></defs>
        <polyline points="28,78 6,90 6,198 110,256 128,246" fill="none" stroke="var(--orange)" stroke-width="2"/>
        <polygon points="142,15 260,80 260,195 142,258 24,195 24,80" fill="url(#g-junk)" stroke="#1b1b1b" stroke-width="4"/>
      </svg>
      <svg class="abs" style="left:340px;top:18px" width="60" height="50" viewBox="0 0 60 50"><polygon points="12,18 23,24 23,36 12,42 1,36 1,24" fill="none" stroke="var(--orange)" stroke-width="1.5"/><polygon points="48,1 56,5 56,13 48,17 40,13 40,5" fill="#d9d9df"/></svg>
      <h3 class="service-title">Junk Removal</h3>
      <div class="service-rule"></div>
      <ul class="service-list">
        <li>Misc. Household Junk</li><li>Hot Tub Removal</li>
        <li>Furniture Removal</li><li>Yard Debris Removal</li>
        <li>Matterss Removal</li><li>Remodeling Debris</li>
        <li>Matterss Removal</li><li>Construction Debris</li>
      </ul>
      <svg class="squiggle" width="68" height="14" viewBox="0 0 68 14"><path d="M2 9 C18 2 30 12 44 7 S60 4 66 6" fill="none" stroke="var(--orange)" stroke-width="4" stroke-linecap="round"/></svg>
    </article>

    <article class="service" style="top:679px">
      <svg class="service-hex" viewBox="0 0 270 260" role="img" aria-label="Moving boxes stacked in an emptied room">
        <defs><linearGradient id="g-boxes" x1="0" y1="0" x2="0" y2="1"><stop offset="0" stop-color="#e8e2da"/><stop offset=".5" stop-color="#c89a6a"/><stop offset="1" stop-color="#a86a32"/></linearGradient></defs>
        <polyline points="28,78 6,90 6,198 110,256 128,246" fill="none" stroke="var(--orange)" stroke-width="2"/>
        <polygon points="142,15 260,80 260,195 142,258 24,195 24,80" fill="url(#g-boxes)" stroke="#1b1b1b" stroke-width="4"/>
      </svg>
      <svg class="abs" style="left:340px;top:18px" width="60" height="50" viewBox="0 0 60 50"><polygon points="12,18 23,24 23,36 12,42 1,36 1,24" fill="none" stroke="var(--orange)" stroke-width="1.5"/><polygon points="48,1 56,5 56,13 48,17 40,13 40,5" fill="#d9d9df"/></svg>
      <h3 class="service-title">Property Cleanouts</h3>
      <div class="service-rule"></div>
      <ul class="service-list">
        <li>Estate Cleanout</li><li>Foreclosure Cleanout</li>
        <li>Residential Cleanout</li><li>Hoarder Cleanout</li>
        <li>Garage Cleanout</li><li>Attic Cleanout</li>
        <li>Storage Unit Cleanout</li><li>Basement Cleanout</li>
      </ul>
      <svg class="squiggle" width="68" height="14" viewBox="0 0 68 14"><path d="M2 9 C18 2 30 12 44 7 S60 4 66 6" fill="none" stroke="var(--orange)" stroke-width="4" stroke-linecap="round"/></svg>
    </article>

    <article class="service" style="top:1225px">
      <svg class="service-hex" viewBox="0 0 270 260" role="img" aria-label="Weathered old wooden shed ready for tear down">
        <defs><linearGradient id="g-shed" x1="0" y1="0" x2="0" y2="1"><stop offset="0" stop-color="#a7b4b8"/><stop offset=".45" stop-color="#8a7e72"/><stop offset="1" stop-color="#55613a"/></linearGradient></defs>
        <polyline points="28,78 6,90 6,198 110,256 128,246" fill="none" stroke="var(--orange)" stroke-width="2"/>
        <polygon points="142,15 260,80 260,195 142,258 24,195 24,80" fill="url(#g-shed)" stroke="#1b1b1b" stroke-width="4"/>
      </svg>
      <svg class="abs" style="left:340px;top:18px" width="60" height="50" viewBox="0 0 60 50"><polygon points="12,18 23,24 23,36 12,42 1,36 1,24" fill="none" stroke="var(--orange)" stroke-width="1.5"/><polygon points="48,1 56,5 56,13 48,17 40,13 40,5" fill="#d9d9df"/></svg>
      <h3 class="service-title">Light Demolition &amp; Tear Down</h3>
      <div class="service-rule"></div>
      <ul class="service-list">
        <li>Shed Removel</li><li>Play Structure Removal</li>
        <li>Fence Removal</li><li>Swing Set Removal</li>
        <li>Deck Removal</li><li>Gazebo Removal</li>
        <li>Hot Tub Removal</li><li>Above Ground Pool</li>
      </ul>
      <svg class="squiggle" width="68" height="14" viewBox="0 0 68 14"><path d="M2 9 C18 2 30 12 44 7 S60 4 66 6" fill="none" stroke="var(--orange)" stroke-width="4" stroke-linecap="round"/></svg>
    </article>
  </section>
</section>

<section class="screen-contact">
  <div class="footer" role="img" aria-label="Dark mountain landscape at dusk"></div>
  <div class="footer-card"></div>

  <div class="quote-card">
    <div class="quote-mark">“</div>
    <p class="quote-text">Lorem ipsum dolor sit amet, consectetur adipiscing elit. Nullam ac tellus urna. Phasellus dictum et purus iaculis accumsan. Sed suscipit pharetra dolor in venenatis. Vivamus eget finibus ipsum, quis placerat sem. Nulla varius erat in libero ornare dignissim. Nam a interdum.</p>
  </div>
  <div class="avatar" role="img" aria-label="Customer portrait"></div>
  <div class="reviewer">DANA WHITFIELD, CO-FOUNDER<small>Lumenfield</small></div>
  <div class="dots"><span class="on"></span><span></span><span></span></div>
  <div class="divider-orange"></div>

  <h2 class="contact-title">CONTACT</h2>
  <p class="contact-sub">Lorem ipsum dolor sit amet, consectetur adipiscing.</p>
  <p class="form-lead">Feel Free to Contact Us</p>
  <div class="field" style="top:514px;height:28px">Name</div>
  <div class="field" style="top:554px;height:28px">Email</div>
  <div class="field" style="top:593px;height:28px">Subject</div>
  <div class="field" style="top:632px;height:86px">Message...</div>
  <div class="btn-submit">SUBMIT</div>

  <div class="footer-brand"><i></i>BRIGHTMOOR<br>JUNK CARTERS</div>
  <p class="footer-text">Lorem ipsum dolor sit amet, consectetur adipiscing elit. Aenean massa mauris, maximus nec faucibus.</p>
  <div class="foot-head" style="left:31px">SITELINKS</div>
  <div class="foot-head" style="left:239px">STAY IN TOUCH</div>
  <div class="foot-links">Home<span>|</span>Our Services<br>What We Take<span>|</span>Contact</div>
  <div class="newsletter-label">Subscribe Our Newsletter</div>
  <div class="newsletter"><b>Subscribe</b></div>
  <div class="footer-bottom">
    <div class="copyright">@ 2021 Brightmoor Junk Carters. All Rights Reserved.</div>
    <div class="social"><span></span><span></span><span></span></div>
  </div>
</section>
</body>
</html>
```